Advertisement Coaching practice

I need an advertisement (to be printed in newspaper). I have a coaching practice where I offer coaching, workshops family constellations and relationship therapy. The ad needs to express calmness, inspiration to transform but also not dull and boring. It would be great if you could use the colors from my logo into the ad.

Dimensions are: 13,04 cm Width x 9,72 cm Height.

I will add my previous self-made ad, my company logo, a portrait photo of myself and the text I want to add. Also my contact details should be visible as well.

Requirements
Nice to have
• I have updated the brief with a flyer that I had previously made by a designer. It would be a nice to have if the ad ties in with that. You can also look at my website at www.fernbrook.nu to see what colors I used there.

```html
<!DOCTYPE html>
<html lang="nl">
<head>
<meta charset="utf-8">
<title>Fernbrook – Coaching advertentie</title>
<link href="https://fonts.googleapis.com/css2?family=Poppins:wght@500;600;800&family=Source+Sans+3:wght@400&family=Caveat:wght@400&display=swap" rel="stylesheet">
<style>
  :root {
    --gold-top: #b39a4f;
    --gold-bottom: #dcc47c;
    --navy: #0e4a6e;
    --white: #ffffff;
    --ink: #111111;
    --grey: #555555;
    --icon-blue: #2a6f97;
    --photo-a: #8d8275;
    --photo-b: #b9c3d3;
  }
  * { margin: 0; padding: 0; box-sizing: border-box; }
  html, body { width: 1200px; height: 895px; overflow: hidden; background: #ffffff; }
  .ad {
    position: relative;
    width: 1200px; height: 895px;
    background: linear-gradient(180deg, var(--gold-top) 0%, var(--gold-bottom) 100%);
    font-family: 'Poppins', sans-serif;
    overflow: hidden;
  }
  .brand {
    position: absolute; left: 808px; top: 23px; width: 392px; height: 114px;
    background: var(--white);
    border-radius: 57px 0 0 57px;
    display: flex; align-items: center; gap: 16px; padding-left: 46px;
  }
  .brand-dot { width: 56px; height: 56px; border-radius: 50%; border: 3px solid var(--grey); }
  .brand-name {
    font-family: 'Source Sans 3', sans-serif; font-weight: 400;
    font-size: 46px; color: var(--grey); letter-spacing: 0.5px;
  }
  .headline {
    position: absolute; left: 52px; top: 79px;
    font-weight: 800; font-size: 46px; line-height: 55px;
    color: var(--navy); text-transform: uppercase; white-space: nowrap;
  }
  .copy {
    position: absolute; left: 46px; top: 258px; width: 670px;
    color: var(--white); font-weight: 500; font-size: 26.5px; line-height: 31.4px;
    white-space: nowrap;
  }
  .copy p + p, .copy p + .intro, .copy ul + p { margin-top: 31.4px; }
  .intro { text-transform: uppercase; font-size: 25px; }
  .benefits { list-style: none; }
  .benefits li { position: relative; padding-left: 29px; }
  .benefits li::before {
    content: ""; position: absolute; left: 0; top: 8px;
    border-left: 14px solid var(--icon-blue);
    border-top: 8px solid transparent; border-bottom: 8px solid transparent;
  }
  .portrait {
    position: absolute; left: 742px; top: 193px; width: 403px; height: 567px;
    border: 6px solid var(--navy); border-radius: 40px;
    background: linear-gradient(180deg, var(--photo-a) 0%, #a08a78 55%, var(--photo-b) 100%);
  }
  .accent-line { position: absolute; left: 0; top: 0; width: 1200px; height: 895px; pointer-events: none; }
  .signature {
    position: absolute; left: 780px; top: 764px; width: 330px; text-align: center;
    font-family: 'Caveat', cursive; font-size: 46px; color: var(--white);
  }
  .contact-bar {
    position: absolute; left: 0; top: 831px; width: 1200px; height: 64px;
    background: var(--white);
    display: flex; align-items: center; justify-content: center; gap: 16px;
    font-weight: 800; font-size: 23.5px; color: var(--ink);
  }
  .contact-item { display: flex; align-items: center; gap: 14px; }
  .contact-item svg { flex: none; }
</style>
</head>
<body>
<div class="ad">
  <div class="brand">
    <span class="brand-dot"></span>
    <span class="brand-name">fernbrook</span>
  </div>

  <h1 class="headline">Coaching,<br>Familieopstellingen<br>&amp; Relatietherapie</h1>

  <div class="copy">
    <p>Trauma’s en negatieve ervaringen vormen ons<br>en blijven nog lang voelbaar. Ze kunnen groei of<br>geluk in de weg staan.</p>
    <p class="intro">Ik ben Anjali en ondersteun je bij het:</p>
    <ul class="benefits">
      <li>Doorbreken van belemmerende patronen;</li>
      <li>Beter omgaan met conflicten;</li>
      <li>In gezonde verbinding met elkaar als koppel<br>of met anderen komen;</li>
    </ul>
    <p>Maandelijks geef ik workshops familieop-<br>stellingen. Ook houd ik themasessies rond<br>adoptie, moeder-dochterdynamiek of relaties.<br>Ook bied ik individuele coaching, relatietherapie<br>en retraites aan. Kijk op de website voor meer<br>info of neem contact op en ontdek wat het<br>beste bij jou past.</p>
  </div>

  <div class="portrait" role="img" aria-label="Portretfoto van de coach"></div>
  <svg class="accent-line" viewBox="0 0 1200 895" aria-hidden="true">
    <line x1="1200" y1="467" x2="955" y2="605" stroke="#ffffff" stroke-width="2"/>
  </svg>
  <div class="signature">Anjali Verhoef</div>

  <div class="contact-bar">
    <span class="contact-item">
      <svg width="40" height="40" viewBox="0 0 40 40" aria-hidden="true">
        <circle cx="20" cy="20" r="18" fill="none" stroke="var(--icon-blue)" stroke-width="2.5"/>
        <path d="M14 11c1.5-1 3-.5 3.5 1l1.2 3c.4 1-.2 1.8-1 2.3 1 2.3 2.7 4 5 5 .5-.8 1.3-1.4 2.3-1l3 1.2c1.5.5 2 2 1 3.5-1.5 2-3.5 2.5-6 1.3-4.5-2.2-8-5.7-10.2-10.2C11.5 14.5 12 12.5 14 11z" fill="var(--icon-blue)"/>
      </svg>
      06-12 34 56 78
    </span>
    <span class="contact-item">
      <svg width="48" height="34" viewBox="0 0 52 36" aria-hidden="true">
        <rect x="2" y="2" width="48" height="32" fill="none" stroke="var(--icon-blue)" stroke-width="2.5"/>
        <path d="M2 2l24 19L50 2M2 34l18-16M50 34L32 18" fill="none" stroke="var(--icon-blue)" stroke-width="2.5"/>
      </svg>
      info@fernbrook.nu
    </span>
    <span class="contact-item">
      <svg width="40" height="40" viewBox="0 0 42 42" aria-hidden="true">
        <g fill="none" stroke="var(--icon-blue)" stroke-width="2.2">
          <circle cx="21" cy="21" r="18"/>
          <ellipse cx="21" cy="21" rx="8" ry="18"/>
          <line x1="21" y1="3" x2="21" y2="39"/>
          <line x1="3" y1="21" x2="39" y2="21"/>
          <path d="M6 12h30M6 30h30"/>
        </g>
      </svg>
      www.fernbrook.nu
    </span>
  </div>
</div>
</body>
</html>
```